My name is Delia Forsythe,I want to create a web page for my personal dog grooming business. The name on the web page can be "Delia's Dog Grooming" I am located in San Antonio Texas. The page would help grow my customer base. Before and after pictures would display the quality of work that I do. On my page I can provide information about myself, my services, and pricing.
Updates

I have updated project to guaranteed pay

Please try to incorporate a schnauzer in an icon or logo. My dog is a schnauzer. THANKS!!!!!!!!!!!!

Target Market(s)

Dog Owners

Industry/Entity Type

Business

Requirements
Must have
• -A spot for before and after pictures.
-An about me section
-A section to make an appointment
Nice to have
• My favorite Color is purple. I think different shades of purple would be nice or purple with a light green

please incorporate a schnauzer in any icon or logo. My dog is a schnauzer.

```html
<!DOCTYPE html>
<html lang="en">
<head>
<meta charset="utf-8">
<title>Delia's Dog Grooming</title>
<link href="https://fonts.googleapis.com/css2?family=Arimo:wght@400;700&display=swap" rel="stylesheet">
<style>
  :root {
    --plum-deep: #3a0f4a;
    --plum: #5e1470;
    --violet: #8e1f9e;
    --violet-light: #b552c2;
    --leaf: #1aa34a;
    --leaf-text: #0aa04a;
    --mint: #c4e3b4;
    --mint-mid: #d9efcf;
    --mint-pale: #eef8ea;
    --sky: #5cc3ef;
    --sky-pale: #c6ecfb;
    --ink: #2a0b36;
    --white: #ffffff;
    --field: #e2e0e4;
  }
  * { box-sizing: border-box; margin: 0; padding: 0; }
  html, body { width: 893px; height: 1200px; overflow: hidden; }
  html { background: var(--white); }
  body { font-family: "Arimo", Arial, sans-serif; position: relative; }

  .page-wash {
    position: absolute; left: 0; top: 900px; width: 893px; height: 300px;
    background: linear-gradient(180deg, var(--white) 0%, var(--mint-pale) 45%, var(--mint-mid) 55%, var(--mint) 100%);
  }

  .site-header {
    position: absolute; left: 0; top: 0; width: 893px; height: 255px;
    background: linear-gradient(180deg, var(--plum-deep) 0%, #4c1a5e 45%, #a98ab3 80%, var(--white) 100%);
  }
  .paw {
    position: absolute; border-radius: 50%;
    background: radial-gradient(circle, var(--sky-pale) 0%, var(--sky) 70%, #2a8ec4 100%);
    border: 3px solid #111;
  }
  .paw--xl { left: 14px; top: 14px; width: 209px; height: 216px; border-width: 6px; }
  .paw--lg { left: 220px; top: 11px; width: 122px; height: 126px; border-width: 5px; }
  .paw--md { left: 360px; top: 11px; width: 93px; height: 94px; border-width: 4px; }
  .paw--sm { left: 481px; top: 14px; width: 74px; height: 67px; }
  .paw--xs { left: 589px; top: 11px; width: 49px; height: 52px; border-width: 2px; }

  .login-field {
    position: absolute; left: 657px; top: 22px; width: 187px; height: 31px;
    background: var(--field);
  }
  .login-link {
    position: absolute; left: 657px; top: 58px; width: 187px; text-align: center;
    color: var(--white); font-weight: 700; font-size: 15px;
  }
  .brand {
    position: absolute; left: 350px; top: 80px; width: 390px; text-align: center;
    color: var(--white); font-weight: 400; line-height: 1;
  }
  .brand__name { display: block; font-size: 62px; }
  .brand__trade { display: block; font-size: 46px; margin-top: 8px; }

  .rule { position: absolute; left: 0; width: 893px; height: 5px; background: var(--leaf); }
  .rule--top { top: 253px; }
  .rule--bottom { top: 1063px; }

  .main-nav { position: absolute; left: 181px; top: 227px; display: flex; gap: 7px; }
  .main-nav a {
    display: block; width: 127px; height: 52px; line-height: 52px; text-align: center;
    color: var(--white); font-weight: 700; font-size: 16px; text-decoration: none;
    background: linear-gradient(180deg, var(--violet-light) 0%, var(--violet) 40%, var(--plum) 100%);
    border: 1px solid var(--plum-deep);
    box-shadow: 0 14px 14px -6px rgba(142, 31, 158, 0.35);
  }

  .portrait {
    position: absolute; left: 63px; top: 317px; width: 364px; height: 450px;
    background: linear-gradient(160deg, #6f7a3c 0%, #3e3a22 45%, #1c1a1a 100%);
  }
  .portrait-caption { position: absolute; left: 60px; top: 776px; font-size: 24px; color: var(--plum); }

  .tagline { position: absolute; left: 472px; top: 313px; font-size: 42px; font-weight: 400; color: var(--plum); }
  .about { position: absolute; left: 477px; top: 383px; width: 362px; }
  .about h2 { font-size: 31px; font-weight: 400; color: var(--plum); margin-bottom: 28px; }
  .about p { font-size: 19.5px; line-height: 31.3px; color: var(--leaf-text); }

  .gallery { position: absolute; top: 822px; left: 0; width: 893px; height: 199px; }
  .gallery__item { position: absolute; top: 0; height: 199px; }
  .gallery__item--1 { left: 35px; width: 223px; background: linear-gradient(160deg, #7a5a3a, #d9d6d0); }
  .gallery__item--2 { left: 273px; width: 173px; background: linear-gradient(160deg, #b9ad98, #e9e6e2); }
  .gallery__item--3 { left: 463px; width: 173px; background: linear-gradient(160deg, #1f3a18, #efefef 55%, #2b4a1f); }
  .gallery__item--4 { left: 653px; width: 212px; background: linear-gradient(180deg, #8f97a0 0%, #b7b3ad 60%, #6c7a3a 100%); }

  .faq { position: absolute; left: 35px; top: 1080px; color: var(--ink); }
  .faq h3 { font-size: 26px; font-weight: 400; margin-bottom: 12px; }
  .faq p { font-size: 20px; line-height: 20px; width: 260px; }

  .social { position: absolute; left: 474px; top: 1080px; color: var(--ink); }
  .social h3 { font-size: 26px; font-weight: 400; margin-left: 98px; margin-bottom: 8px; }
  .social ul { list-style: none; display: flex; align-items: center; gap: 10px; }
  .social li { display: flex; align-items: center; gap: 10px; font-size: 33px; font-weight: 700; }
  .social li::before {
    content: ""; width: 44px; height: 44px; border-radius: 6px; background: var(--plum);
  }
</style>
</head>
<body>
  <div class="page-wash"></div>

  <header class="site-header">
    <div class="paw paw--xl" role="img" aria-label="Paw print badge with schnauzer illustration"></div>
    <div class="paw paw--lg" role="img" aria-label="Paw print badge with schnauzer illustration"></div>
    <div class="paw paw--md" role="img" aria-label="Paw print badge with schnauzer illustration"></div>
    <div class="paw paw--sm" role="img" aria-label="Paw print badge with schnauzer illustration"></div>
    <div class="paw paw--xs" role="img" aria-label="Paw print badge with schnauzer illustration"></div>

    <div class="login-field"></div>
    <div class="login-link">LOG ON / SIGN IN</div>

    <h1 class="brand">
      <span class="brand__name">Delia's</span>
      <span class="brand__trade">Dog Grooming</span>
    </h1>
  </header>
  <div class="rule rule--top"></div>

  <nav class="main-nav">
    <a href="#">Home</a>
    <a href="#">About Us</a>
    <a href="#">Services</a>
    <a href="#">Contact Us</a>
  </nav>

  <div class="portrait" role="img" aria-label="Photo of the groomer holding her schnauzer outdoors"></div>
  <div class="portrait-caption">Your photo here</div>

  <div class="tagline">Your tag line here..</div>
  <section class="about">
    <h2>About Me</h2>
    <p>My name is Delia Forsythe,I want to create a web page for my personal dog grooming business. The name on the web page can be "Delia's Dog Grooming" I am located in San Antonio Texas. The page would help grow my customer base. Before and after pictures would display the quality of work that I do. On my page I can provide information about myself, my services, and pricing.</p>
  </section>

  <section class="gallery">
    <div class="gallery__item gallery__item--1" role="img" aria-label="Groomed schnauzer puppy on a blanket"></div>
    <div class="gallery__item gallery__item--2" role="img" aria-label="Two schnauzers sitting together"></div>
    <div class="gallery__item gallery__item--3" role="img" aria-label="White schnauzer close-up"></div>
    <div class="gallery__item gallery__item--4" role="img" aria-label="Schnauzer standing on grass"></div>
  </section>

  <div class="rule rule--bottom"></div>
  <footer>
    <div class="faq">
      <h3>FQA</h3>
      <p>FAQ for dog owners who want to know more</p>
    </div>
    <div class="social">
      <h3>Follow us on:</h3>
      <ul>
        <li>Pawbook</li>
        <li>Chirper</li>
      </ul>
    </div>
  </footer>
</body>
</html>
```